Saffron Ledger Works Flyer

We need a one page promotional piece that explains what our company does, and the benefits it provides in a simple, elegant, easy to understand way. I would like to print it on glossy heavyweight paper to give a feel of high quality and legitimacy. I will include the logo, the tag line, and the main benefits that the company offers.

Tag line concept, may not need these exact words. "Give us 5 minutes a day, and we will help you build a Saffron Ledger Works."

Key points...(exact wording not required if you think of a better way to say it)

Software easy enough for my grandpa to use.
Lets you use snail mail, email, texting, and social media to quickly market to your customers at very low cost.
Web based which allows you to launch media campaigns from your desktop, or smartphone in moments.
Quick 3 - 5 minute training videos which give you hard hitting, quick action tips that will help you make your business better today.
Live coaching calls to help motivate you to improve your business.
No contracts, or start up fees. One low price of $299 per month.

Restaurant owners

Restaurant

```html
<!DOCTYPE html>
<html lang="en">
<head>
<meta charset="utf-8">
<title>Saffron Ledger Works Flyer</title>
<link rel="stylesheet" href="https://fonts.googleapis.com/css2?family=Cormorant+Garamond:ital,wght@1,500;1,600&family=Big+Shoulders+Display:wght@300;800&display=swap">
<style>
  :root {
    --page-bg-top: #ffffff;
    --page-bg-bottom: #e4e4e4;
    --panel-dark: #1c1c1c;
    --panel-mid: #2f2f2f;
    --band-green: #6aaa50;
    --brand-green: #78b04a;
    --tag-green: #7fb447;
    --body-text: #f2f2f2;
    --coin-yellow: #d4dc16;
    --coin-green: #5f9e1c;
  }
  * { box-sizing: border-box; margin: 0; padding: 0; }
  html, body { width: 1000px; height: 1200px; overflow: hidden; }
  body {
    position: relative;
    background: linear-gradient(180deg, var(--page-bg-top) 0%, var(--page-bg-bottom) 100%);
    font-family: "Cormorant Garamond", Georgia, serif;
  }
  .flyer {
    position: absolute;
    left: 128px; top: 45px;
    width: 742px; height: 1112px;
    background:
      radial-gradient(ellipse at 45% 55%, var(--panel-mid) 0%, var(--panel-dark) 75%),
      var(--panel-dark);
    overflow: hidden;
    box-shadow: 0 0 2px rgba(0,0,0,.5);
  }
  .header-band {
    position: absolute;
    left: 6px; top: 29px;
    width: 717px; height: 173px;
    background: var(--band-green);
  }
  .brand {
    position: absolute;
    left: 0; right: 0; top: 214px;
    display: flex; align-items: center; justify-content: center; gap: 14px;
  }
  .brand-dot {
    width: 18px; height: 18px; border-radius: 50%;
    background: var(--brand-green);
  }
  .brand-name {
    font-style: italic; font-weight: 600;
    font-size: 40px; letter-spacing: 2px;
    color: var(--brand-green);
  }
  .benefits {
    position: absolute;
    left: 31px; top: 302px;
    width: 680px;
    list-style: none;
    color: var(--body-text);
    font-style: italic; font-weight: 500;
    font-size: 26px; line-height: 32px;
    letter-spacing: 6px;
  }
  .benefits li { margin-bottom: 10px; }
  .coin-art {
    position: absolute;
    left: 352px; top: 843px;
    width: 420px; height: 300px;
    border-radius: 60% 40% 0 0 / 70% 45% 0 0;
    background: radial-gradient(ellipse at 40% 45%, var(--coin-yellow) 0%, var(--coin-green) 80%);
  }
  .tagline {
    position: absolute;
    left: 22px; top: 884px;
    width: 320px;
    font-family: "Big Shoulders Display", "Arial Narrow", sans-serif;
    font-weight: 300;
    text-transform: uppercase;
    color: var(--tag-green);
    font-size: 34px; line-height: 49px;
    letter-spacing: 3px;
    white-space: nowrap;
  }
  .tagline strong { font-weight: 800; }
</style>
</head>
<body>
  <main class="flyer">
    <div class="header-band"></div>
    <div class="brand">
      <span class="brand-dot"></span>
      <span class="brand-name">Saffron Ledger Works</span>
    </div>
    <ul class="benefits">
      <li>Software easy enough for my grandpa to use.</li>
      <li>Lets you use snail mail, email, texting and social media to quickly market to your customers at very low cost.</li>
      <li>Web based which allows you launch media campaigns from your desktop, or smart-phone in moments.</li>
      <li>Quick 3-5 minute training videos which give you hard hitting, quick action tips that will help you make your business better today.</li>
      <li>Live coaching calls to help motivate you to improve your business.</li>
      <li>No contracts or start up fees. One low price of $299 per month.</li>
    </ul>
    <div class="coin-art" role="img" aria-label="Large glossy green and yellow dollar sign illustration"></div>
    <p class="tagline">Give us 5 minutes a day,<br>and we will help you<br>build a <strong>Saffron</strong><br><strong>Ledger Works!</strong></p>
  </main>
</body>
</html>
```